TRUCKING/TRANSPORTATION COMPANY BUSINESS CARD.

We need a business card design for our trucking company based in Tupelo, MS.
It will be a double sided design.
FRONT SIDE:
We need a good looking logo with a tagline. The tagline should match the type of business.
COMPANY NAME: RD HAULING LLC
BACK SIDE:
The following information should be displayed on the back of the card.
Office: 662.555.0187
Mailing: 214 W. Elm Ave.
Tupelo, MS 38899
Email: rdhaulllc@mailbox-demo.com
Trucking Company
FRONT SIDE:
BACK SIDE:
Office: 662.555.0187
Mailing: 214 W. Elm Ave.
Tupelo, MS 38899

```html
<!DOCTYPE html>
<html lang="en">
<head>
<meta charset="utf-8">
<title>RD Hauling LLC – Business Card</title>
<link rel="stylesheet" href="https://fonts.googleapis.com/css2?family=Lato:wght@400;700;900&display=swap">
<style>
  :root {
    --teal: #1cb191;
    --teal-dark: #139a7e;
    --charcoal: #333335;
    --ink: #151515;
    --white: #ffffff;
    --page: #e9e4da;
    --rule: #8a6a3a;
  }
  * { box-sizing: border-box; margin: 0; padding: 0; }
  html, body { width: 1200px; height: 900px; overflow: hidden; }
  body {
    background: var(--page);
    font-family: "Lato", sans-serif;
    position: relative;
  }
  .card {
    position: absolute;
    width: 620px;
    height: 355px;
    overflow: hidden;
    box-shadow: 0 8px 22px rgba(0,0,0,.28);
  }
  .card--front { left: 60px; top: 70px; background: var(--charcoal); }
  .card--back { left: 520px; top: 475px; background: var(--white); }

  /* Front */
  .front-panel {
    position: absolute; left: 0; right: 0; top: 62px; height: 236px;
    background: var(--teal);
  }
  .front-strip {
    position: absolute; left: 0; right: 0; top: 210px; height: 88px;
    background: var(--teal-dark);
  }
  .front-notch {
    position: absolute; left: 300px; top: 196px;
    width: 0; height: 0;
    border-left: 16px solid transparent;
    border-right: 16px solid transparent;
    border-bottom: 14px solid var(--teal-dark);
  }
  .brand {
    position: absolute; left: 0; right: 0;
    display: flex; align-items: center; justify-content: center; gap: 12px;
  }
  .brand__dot {
    width: 34px; height: 34px; border-radius: 50%;
    background: var(--ink);
  }
  .brand__name {
    font-weight: 900; color: var(--ink);
    font-size: 38px; letter-spacing: .5px; white-space: nowrap;
  }
  .card--front .brand { top: 120px; }
  .rule {
    position: absolute; height: 2px; background: var(--rule);
  }
  .card--front .rule { left: 170px; width: 300px; top: 178px; }
  .tagline {
    position: absolute; left: 0; right: 0; text-align: center;
    font-weight: 700; color: var(--ink); font-size: 16px; white-space: nowrap;
  }
  .card--front .tagline { top: 240px; }

  /* Back */
  .card--back .brand { top: 88px; }
  .card--back .brand__name { font-size: 34px; }
  .card--back .rule { left: 180px; width: 280px; top: 140px; }
  .card--back .tagline { top: 150px; font-size: 15px; }
  .back-dark {
    position: absolute; left: 0; right: 0; top: 200px; bottom: 0;
    background: var(--charcoal);
  }
  .back-band {
    position: absolute; left: 0; right: 0; top: 200px; height: 44px;
    background: var(--teal);
  }
  .contact {
    position: absolute; display: flex; align-items: center; gap: 10px;
    color: var(--white); font-size: 17px; white-space: nowrap;
  }
  .contact svg { flex: none; }
  .contact--address { left: 18px; top: 209px; }
  .contact--email { left: 350px; top: 209px; font-size: 15px; }
  .contact--phone { left: 70px; top: 272px; }
  .back-line {
    position: absolute; left: 60px; right: 60px; bottom: 28px; height: 5px;
    background: var(--teal);
  }
</style>
</head>
<body>

<section class="card card--front" aria-label="Card front">
  <div class="front-panel"></div>
  <div class="front-strip"></div>
  <div class="front-notch"></div>
  <div class="brand">
    <span class="brand__dot"></span>
    <span class="brand__name">RD HAULING LLC</span>
  </div>
  <div class="rule"></div>
  <p class="tagline">Every Load On Time, Every Mile, Every Day</p>
</section>

<section class="card card--back" aria-label="Card back">
  <div class="brand">
    <span class="brand__dot"></span>
    <span class="brand__name">RD HAULING LLC</span>
  </div>
  <div class="rule"></div>
  <p class="tagline">Every Load On Time, Every Mile, Every Day</p>

  <div class="back-dark"></div>
  <div class="back-band"></div>

  <div class="contact contact--address">
    <svg width="26" height="26" viewBox="0 0 26 26" aria-hidden="true">
      <rect x="0" y="0" width="26" height="26" fill="#2a8f78"/>
      <rect x="5" y="5" width="16" height="17" fill="#fff"/>
      <g fill="#2a8f78">
        <rect x="8" y="8" width="3" height="3"/><rect x="15" y="8" width="3" height="3"/>
        <rect x="8" y="13" width="3" height="3"/><rect x="15" y="13" width="3" height="3"/>
        <rect x="11.5" y="18" width="3" height="4"/>
      </g>
    </svg>
    <span>214 W. Elm Ave. Tupelo, MS 38899</span>
  </div>

  <div class="contact contact--email">
    <svg width="18" height="13" viewBox="0 0 18 13" aria-hidden="true">
      <rect x="0.5" y="0.5" width="17" height="12" fill="none" stroke="#fff"/>
      <path d="M1 1 L9 7.5 L17 1" fill="none" stroke="#fff"/>
    </svg>
    <span>rdhaulllc@mailbox-demo.com</span>
  </div>

  <div class="contact contact--phone">
    <svg width="18" height="16" viewBox="0 0 18 16" aria-hidden="true">
      <path d="M2 5 Q9 0 16 5 L14 7 L12 5 L6 5 L4 7 Z" fill="#fff"/>
      <rect x="3" y="8" width="12" height="7" rx="1" fill="#fff"/>
    </svg>
    <span>662.555.0187</span>
  </div>

  <div class="back-line"></div>
</section>

</body>
</html>
```